Creative Business Card

Were looking for a new fresh and creative look to our Business card. Our company name is InkHollow. Be creative, Were attaching our logo and our base colors, but your free to do anything. Name, title, Phone

Industry/Entity Type

Business

```html
<!DOCTYPE html>
<html lang="en">
<head>
<meta charset="utf-8">
<title>InkHollow Business Card</title>
<link rel="stylesheet" href="https://fonts.googleapis.com/css2?family=Lato:ital,wght@0,400;0,700;0,900;1,700&display=swap">
<style>
  :root {
    --backdrop: #e4e6e8;
    --card-white: #ffffff;
    --brand-blue: #0a74c0;
    --brand-green: #7cc242;
    --text-white: #ffffff;
    --card-shadow: rgba(0, 0, 0, 0.18);
  }
  * { margin: 0; padding: 0; box-sizing: border-box; }
  html, body {
    width: 1200px;
    height: 926px;
    overflow: hidden;
    background: var(--backdrop);
    font-family: "Lato", sans-serif;
  }
  .canvas {
    position: relative;
    width: 1200px;
    height: 926px;
  }
  .card {
    position: absolute;
    left: 320px;
    width: 560px;
    height: 320px;
    background: var(--card-white);
    overflow: hidden;
    box-shadow: 0 6px 18px var(--card-shadow);
  }
  .card-front { top: 100px; }
  .card-back { top: 500px; }

  .wordmark {
    position: absolute;
    left: 0;
    right: 0;
    text-align: center;
    font-weight: 900;
    color: var(--brand-green);
    letter-spacing: 1px;
    line-height: 1;
  }
  .card-front .wordmark { top: 92px; font-size: 58px; }
  .card-back .wordmark { top: 30px; font-size: 50px; }

  .front-swoosh {
    position: absolute;
    left: 0;
    bottom: 0;
    width: 560px;
    height: 150px;
  }
  .front-website {
    position: absolute;
    left: 0;
    right: 0;
    bottom: 58px;
    text-align: center;
    color: var(--text-white);
    font-size: 13px;
    font-weight: 700;
    letter-spacing: 1.5px;
  }

  .back-stripe {
    position: absolute;
    left: 0;
    top: 106px;
    width: 100%;
    height: 8px;
    background: var(--brand-green);
  }
  .back-panel {
    position: absolute;
    left: 0;
    top: 114px;
    width: 100%;
    bottom: 0;
    background: var(--brand-blue);
    color: var(--text-white);
    text-align: center;
    padding-top: 22px;
  }
  .contact-name {
    font-size: 30px;
    font-weight: 400;
    line-height: 1.1;
    margin-bottom: 10px;
  }
  .contact-name strong { font-weight: 700; }
  .contact-line {
    font-size: 15px;
    line-height: 1.45;
  }
  .contact-label {
    font-weight: 700;
    font-style: italic;
  }
</style>
</head>
<body>
<main class="canvas">

  <section class="card card-front" aria-label="Business card front">
    <div class="wordmark">InkHollow</div>
    <svg class="front-swoosh" viewBox="0 0 560 150" preserveAspectRatio="none" aria-hidden="true">
      <path d="M0 70 Q280 -10 560 120 L560 150 L0 150 Z" fill="var(--brand-green)"/>
      <path d="M0 80 Q280 6 560 128 L560 150 L0 150 Z" fill="var(--card-white)"/>
      <path d="M0 86 Q280 14 560 132 L560 150 L0 150 Z" fill="var(--brand-blue)"/>
    </svg>
    <div class="front-website">www.inkhollowprint.com</div>
  </section>

  <section class="card card-back" aria-label="Business card back">
    <div class="wordmark">InkHollow</div>
    <div class="back-stripe"></div>
    <div class="back-panel">
      <p class="contact-name">Maya <strong>Thornton</strong></p>
      <p class="contact-line"><span class="contact-label">phone:</span> 555-214-9086</p>
      <p class="contact-line"><span class="contact-label">web:</span> inkhollowprint.com</p>
      <p class="contact-line"><span class="contact-label">email:</span> maya@inkhollowprint.com</p>
      <p class="contact-line"><span class="contact-label">address:</span> 48 Fernbrook Lane, Suite #210, Cedar Bldg, OR 97214</p>
    </div>
  </section>

</main>
</body>
</html>
```